Corvell Advisory

Business Development Consulting Firm

Target Market(s)

Federal Government, 8(a) companies, Small Businesses

Industry/Entity Type

Private Sector, US Government

Contact Information for Business Card

8(a) Program Capture, Business Development, Industry Trends & Analysis, Strategic Teaming, Cyber Solutions

Colors

Designer to choose colors to be used in the design.

```html
<!DOCTYPE html>
<html lang="en">
<head>
<meta charset="utf-8">
<title>Corvell Advisory Business Card</title>
<link href="https://fonts.googleapis.com/css2?family=Poppins:wght@400;600&display=swap" rel="stylesheet">
<style>
  :root {
    --backdrop: #2b2725;
    --card: #1b1b1b;
    --blue: #0a85d1;
    --green: #6cbf1a;
    --ink: #e8e8e8;
  }
  html, body {
    margin: 0;
    padding: 0;
    width: 1200px;
    height: 842px;
    overflow: hidden;
    background: var(--backdrop);
    font-family: "Poppins", sans-serif;
  }
  .canvas {
    position: relative;
    width: 1200px;
    height: 842px;
  }
  .card {
    position: absolute;
    top: 272px;
    width: 520px;
    height: 298px;
    background: var(--card);
    box-shadow: 0 12px 30px rgba(0,0,0,0.45);
    overflow: hidden;
  }
  .card-back { left: 50px; }
  .card-front { left: 630px; }

  /* contact side */
  .band {
    position: absolute;
    left: 0;
    width: 100%;
    height: 12px;
    background: var(--blue);
  }
  .band-top { top: 0; }
  .band-bottom { bottom: 0; }
  .contact {
    position: absolute;
    inset: 12px 0;
    display: flex;
    flex-direction: column;
    align-items: center;
    justify-content: center;
    text-align: center;
    color: var(--ink);
    text-transform: uppercase;
    letter-spacing: 0.5px;
  }
  .person-name {
    margin: 0;
    color: var(--green);
    font-weight: 600;
    font-size: 22px;
    line-height: 1.1;
  }
  .person-role {
    margin: 2px 0 0;
    font-size: 13px;
    font-weight: 400;
  }
  .rule {
    width: 44px;
    height: 1.5px;
    background: var(--green);
    margin: 10px 0;
  }
  .details p {
    margin: 0;
    font-size: 14px;
    line-height: 1.35;
  }
  .address p {
    margin: 0;
    font-size: 13px;
    line-height: 1.35;
  }
  .address { margin-top: 8px; }

  /* brand side */
  .edge-bar {
    position: absolute;
    top: 92px;
    width: 36px;
    height: 96px;
    background: var(--blue);
  }
  .edge-line {
    position: absolute;
    top: 92px;
    width: 4px;
    height: 96px;
    background: var(--green);
  }
  .edge-left .edge-bar { left: 0; }
  .edge-left .edge-line { left: 44px; }
  .edge-right .edge-bar { right: 0; }
  .edge-right .edge-line { right: 44px; }
  .brand {
    position: absolute;
    inset: 0;
    display: flex;
    align-items: center;
    justify-content: center;
    gap: 12px;
  }
  .brand-square {
    width: 22px;
    height: 22px;
    background: var(--green);
  }
  .brand-name {
    margin: 0;
    color: var(--blue);
    font-weight: 600;
    font-size: 28px;
    letter-spacing: 1px;
    text-transform: uppercase;
  }
</style>
</head>
<body>
<main class="canvas">
  <section class="card card-back" aria-label="Contact side">
    <div class="band band-top"></div>
    <div class="contact">
      <h2 class="person-name">Daniel Harlow</h2>
      <p class="person-role">Managing Director</p>
      <div class="rule"></div>
      <div class="details">
        <p>044-555 210 348</p>
        <p>info@corvelladvisory.com</p>
        <p>www.corvelladvisory.com</p>
      </div>
      <div class="rule"></div>
      <div class="address">
        <p>421, Address Line Goes Here</p>
        <p>45452, Country Name</p>
      </div>
    </div>
    <div class="band band-bottom"></div>
  </section>

  <section class="card card-front" aria-label="Brand side">
    <div class="edge-left">
      <div class="edge-bar"></div>
      <div class="edge-line"></div>
    </div>
    <div class="brand">
      <span class="brand-square"></span>
      <h1 class="brand-name">Corvell Advisory</h1>
    </div>
    <div class="edge-right">
      <div class="edge-bar"></div>
      <div class="edge-line"></div>
    </div>
  </section>
</main>
</body>
</html>
```